Wordpress Powered Website. Outstanding Design Required. Using Morvenix Theme

Designers will not need to create anything other than the home page but there are some design elements on the home page which also need to be factored in: 6 product place holders and 2-3 slides for a slideshow (with images I provide).

Designers will need to familiarise themselves with the Morvenix theme to make sure that their design will work within the theme.

The winning designer will set up all the pages and navigation in place. This includes social media icons, favicon, widgets, etc. In other words, the home page needs to be designed and coded and the other preset theme pages need to be organised in a way that we can start using the website on completion of the job.

Most of the designs I had last time were too colourful. This needs to be subtle not in your face.

Background to the business/website:
Tandrel Banners is a new Australian venture which will sell large format printed banners and other signage. The market is very competitive so it is important to stand out visually and to have a website which is clean, easy to navigate and easy to order. It will be a combination of online sales and assisted sales but all sales enquiries will come from the website.

As our business is focused on presentation it is vital to have excellent design.
Purchased theme is Morvenix. Only this theme is to be used.

1. A home page using all the preset features of the Morvenix theme - it will just be basically taking my wireframe and inputting it to the live theme.
2. A three slide slideshow, ideally with an edited video. The static image slides can be provided by me during the handover. Placeholder for now.
Similar to this one: http://thebrindlecraft.com.au/

Attached is the logo which must be utilised, although it could also sit on a dark background. There is our mascot as well which can be used but does not have to be included.

Target Market(s)

Primarily B2B (business to business)
Main industries will be Construction, Retail, Community, Events & Trade Shows

Industry/Entity Type

Printing

Coding

Coded - Design and coding required

Font styles to use
Sans Serif

Requirements
Must have
• Must have the design files made to web pages within the Wordpress environment.
Nice to have
• Clean design. Stand out from competitors based on design.
Should not have
• Should not look like any competitor

```html
<!DOCTYPE html>
<html lang="en">
<head>
<meta charset="utf-8">
<title>Tandrel Banners – Home</title>
<link rel="stylesheet" href="https://fonts.googleapis.com/css2?family=Montserrat:wght@400;600;700&family=Open+Sans:ital,wght@0,400;0,600;0,700;1,400;1,600&display=swap">
<style>
:root{
  --accent:#f26522;
  --blue:#1a6fd0;
  --blue-card:rgba(255,255,255,.14);
  --ink:#222;
  --muted:#666;
  --light:#f7f7f7;
  --footer:#3b3b3b;
  --footer-deep:#2b2b2b;
  --yellow:#f6c500;
  --white:#fff;
}
*{box-sizing:border-box;margin:0;padding:0}
html,body{width:1200px;height:2804px;overflow:hidden}
body{font-family:"Open Sans",Arial,sans-serif;color:var(--ink);position:relative;background:var(--white)}
.section{position:absolute;left:0;width:1200px}
.abs{position:absolute}
h2.section-title{font-family:"Montserrat",Arial,sans-serif;font-weight:700;font-size:21px;letter-spacing:.5px;text-align:center}
.section-sub{font-size:11px;text-align:center;margin-top:4px;color:var(--muted)}
.title-rule{width:150px;height:1px;background:#ccc;margin:10px auto 0}

/* hero */
.hero{top:0;height:415px;background:
  radial-gradient(ellipse at 15% 70%,#2c7fa0 0,transparent 35%),
  radial-gradient(ellipse at 45% 20%,#b83a8a 0,transparent 35%),
  radial-gradient(ellipse at 75% 60%,#d9a22a 0,transparent 35%),
  radial-gradient(ellipse at 95% 20%,#6b3ab0 0,transparent 30%),
  linear-gradient(135deg,#1b1b1b,#3a2040 50%,#111);}
.topbar{top:0;height:22px;width:1200px;font-size:9px;color:#bbb;background:rgba(0,0,0,.55)}
.topbar span{position:absolute;top:5px}
.header{top:22px;height:60px;width:1200px}
.brand{left:207px;top:18px;display:flex;align-items:center;gap:7px;font-family:"Montserrat",Arial,sans-serif;font-weight:700;font-size:13px;line-height:1.05;color:var(--white);letter-spacing:.5px;width:150px}
.brand-square{width:12px;height:12px;background:var(--accent);flex:none}
.nav{left:385px;top:34px;display:flex;gap:22px;font-size:10px;color:var(--white)}
.nav .active{color:var(--accent);border-bottom:2px solid var(--accent);padding-bottom:8px}
.cart{left:856px;top:33px;font-size:10px;font-weight:700;color:var(--yellow)}
.hero-copy{left:0;width:1200px;top:207px;text-align:center;color:var(--white)}
.hero-copy h1{font-family:"Montserrat",Arial,sans-serif;font-weight:400;font-size:27px}
.hero-copy p{font-family:"Montserrat",Arial,sans-serif;font-size:17px;margin-top:1px}
.btn-ghost{display:inline-block;margin-top:16px;border:2px solid var(--white);border-radius:14px;padding:5px 20px;font-size:9px;font-weight:700;letter-spacing:1px;color:var(--white)}
.dots{left:576px;top:374px;display:flex;gap:5px}
.dots i{width:6px;height:6px;border-radius:50%;background:rgba(255,255,255,.6)}
.dots i:first-child{background:var(--white)}

/* category */
.category{top:415px;height:959px;background:var(--light)}
.category .head{position:absolute;top:48px;width:1200px}
.tile{position:absolute;width:247px;overflow:hidden}
.tag{position:absolute;left:0;top:22px;background:var(--white);font-size:10px;font-weight:700;padding:4px 22px 4px 10px;clip-path:polygon(0 0,100% 0,88% 50%,100% 100%,0 100%)}
.tile-feature{color:var(--white);text-align:center}
.tile-feature .txt{position:absolute;top:76px;width:100%}
.tile-feature h3{font-family:"Montserrat",Arial,sans-serif;font-size:17px;letter-spacing:1.5px}
.tile-feature p{font-size:12px}
.tile-feature .btn-ghost{padding:4px 14px;font-size:8px;margin-top:14px}
.view-all{top:890px;left:0;width:1200px;text-align:center;font-size:11px;text-decoration:underline}

/* about */
.about{top:1374px;height:351px}
.about-title{left:207px;top:48px;font-family:"Montserrat",Arial,sans-serif;font-size:32px;display:flex;align-items:center;gap:10px}
.about-title .brand-name{font-weight:700;font-size:30px;color:var(--accent)}
.about-text{left:207px;top:120px;width:375px;font-size:10px;line-height:1.45;color:#444}
.about-text p+p{margin-top:10px}
.btn-solid{left:207px;top:268px;background:var(--accent);color:var(--white);font-size:9px;font-weight:700;border-radius:12px;padding:6px 16px}
.divider{left:634px;top:36px;width:1px;height:280px;background:#ddd}
.feature{left:677px;width:316px}
.feature .badge{position:absolute;left:0;top:0;width:46px;height:52px;background:var(--yellow);clip-path:polygon(0 0,100% 0,100% 100%,50% 82%,0 100%)}
.feature .badge svg{position:absolute;left:13px;top:12px}
.feature h4{margin-left:70px;font-size:12px;font-weight:700;line-height:1.2}
.feature p{margin-left:70px;margin-top:6px;font-size:10px;color:#555;line-height:1.4}
.feature-rule{left:677px;top:167px;width:316px;height:1px;background:#ddd}

/* testimonials */
.wow{top:1725px;height:475px;background:var(--blue);color:var(--white)}
.wow .head{position:absolute;top:52px;width:1200px}
.wow .section-sub{color:#e5eefa}
.wow .title-rule{background:rgba(255,255,255,.4)}
.quote{position:absolute;background:var(--blue-card);font-style:italic;font-weight:600;font-size:10px;line-height:1.45;padding:20px}
.avatar{position:absolute;border-radius:50%;background:linear-gradient(#c9d6e2,#8aa0b4);border:3px solid var(--white)}
.who{position:absolute;font-size:12px;line-height:1.2}
.who small{display:block;font-size:9px;opacity:.85}
.stars{color:var(--yellow);font-size:10px;letter-spacing:1px}
.view-testi{left:0;width:1200px;top:406px;text-align:center;font-size:11px;font-weight:600}

/* contact strip */
.dedicated{top:2200px;height:271px}
.dedicated .head{position:absolute;top:50px;width:1200px}
.contact-item{position:absolute;top:145px;width:200px;margin-left:-100px;text-align:center}
.contact-item h5{font-size:16px;font-weight:400;margin-top:8px}
.contact-item p{font-size:9px;color:#555;margin-top:3px}

/* footer */
.footer{top:2471px;height:276px;background:var(--footer);color:#ddd}
.rating{left:202px;top:-16px}
.foot-col{position:absolute;top:60px;font-size:10px}
.foot-col h6{font-size:12px;font-weight:600;color:var(--white);padding-bottom:8px;border-bottom:1px solid #555;margin-bottom:10px}
.foot-col li{list-style:none;line-height:1.6}
.foot-col li::before{content:"• ";color:#999}
.foot-col li.current{color:var(--accent)}
.field{width:180px;height:24px;background:#555;border:1px solid #666;margin-top:8px;font-size:9px;color:#bbb;padding:5px 8px}
.send{display:inline-block;margin-top:14px;border:2px solid var(--white);border-radius:12px;padding:3px 20px;font-size:9px;font-weight:700;color:var(--white)}
.social{left:207px;top:225px;display:flex;align-items:center;gap:6px;font-size:10px;color:var(--white)}
.social i{width:16px;height:16px;background:#2f7fd3}
.bottombar{top:2747px;height:57px;background:var(--footer-deep);color:#aaa;font-size:10px}
</style>
</head>
<body>

<!-- Hero -->
<section class="section hero" role="img" aria-label="Slideshow image: colourful woven fabric texture">
  <div class="abs topbar">
    <span style="left:207px">English ⌄ &nbsp;&nbsp;|&nbsp;&nbsp; USD ⌄</span>
    <span style="left:724px">Questions? Call ☏ 555-010-246 &nbsp;|&nbsp; User 🔒 Login / Register</span>
  </div>
  <header class="abs header">
    <div class="abs brand"><span class="brand-square"></span><span>TANDREL<br>BANNERS</span></div>
    <nav class="abs nav">
      <span class="active">Banners &amp; Signs</span><span>Stands &amp; Displays</span><span>Stickers &amp; Posters</span><span>About Us</span><span>Contact Us</span>
      <svg width="12" height="12" viewBox="0 0 12 12"><circle cx="5" cy="5" r="3.5" fill="none" stroke="#fff" stroke-width="1.6"/><path d="M8 8l3 3" stroke="#fff" stroke-width="1.6"/></svg>
    </nav>
    <div class="abs cart">☰ &nbsp;Cart / $2000.00</div>
    <svg class="abs" style="left:968px;top:26px" width="22" height="20" viewBox="0 0 22 20"><path d="M3 6h14l-1.5 12h-11z" fill="none" stroke="#f6c500" stroke-width="2"/><path d="M7 6V4a3 3 0 0 1 6 0v2" fill="none" stroke="#f6c500" stroke-width="2"/><circle cx="18" cy="4" r="4" fill="#1a6fd0"/></svg>
  </header>
  <div class="abs hero-copy">
    <h1>Over 250 Signs &amp; Display</h1>
    <p>Products in custom sizes</p>
    <span class="btn-ghost">SEE ALL PRODUCTS</span>
  </div>
  <div class="abs dots"><i></i><i></i><i></i><i></i><i></i></div>
</section>

<!-- Category -->
<section class="section category">
  <div class="head">
    <h2 class="section-title">CATEGORY</h2>
    <p class="section-sub">Lorem Ipsum is simply dummy text of the printing and typesetting</p>
    <div class="title-rule"></div>
  </div>

  <div class="tile tile-feature" style="left:207px;top:131px;height:252px;background:linear-gradient(135deg,#1a1a1a,#3a3a3a)" role="img" aria-label="Dark abstract banner artwork">
    <div class="txt">
      <h3>BANNERS</h3>
      <p>(900MM x 600MM)</p>
      <p style="font-weight:700">START AT $6.99</p>
      <span class="btn-ghost">START ORDER</span>
    </div>
  </div>
  <div class="tile" style="left:207px;top:404px;height:178px;background:linear-gradient(160deg,#dfe6ec,#5b6670)" role="img" aria-label="Vinyl sticker artwork of a leaping figure"><span class="tag">VINYL STICKERS</span></div>
  <div class="tile" style="left:207px;top:603px;height:252px;background:linear-gradient(160deg,#8a7350,#d8c28a)" role="img" aria-label="Fabric banner photo of pasta on a fork"><span class="tag">FABRIC BANNERS</span></div>

  <div class="tile" style="left:476px;top:131px;height:174px;background:linear-gradient(160deg,#1c1c1c,#6a5a40)" role="img" aria-label="Vinyl sticker photo of a cracked egg"><span class="tag">VINYL STICKERS</span></div>
  <div class="tile" style="left:476px;top:327px;height:331px;background:linear-gradient(160deg,#f0f0f0,#c9cfc9 70%,#2f7d4c)" role="img" aria-label="Wall mural photo of a green handbag on a chair"><span class="tag">WALL MURALS</span></div>
  <div class="tile" style="left:476px;top:680px;height:175px;background:linear-gradient(160deg,#e6e6e6,#9fa59f)" role="img" aria-label="Banner photo of a green leaf shaped like a fish"><span class="tag">BANNERS</span></div>

  <div class="tile" style="left:746px;top:131px;height:252px;background:linear-gradient(160deg,#f4f4f4,#e2e2e2 70%,#c2272d)" role="img" aria-label="Wall mural of blossom branch, birds and red chair"><span class="tag">WALL MURALS</span></div>
  <div class="tile" style="left:746px;top:404px;height:178px;background:linear-gradient(160deg,#f0f0f0,#b9a898)" role="img" aria-label="Fabric banner portrait of a bearded man holding a card"><span class="tag">FABRIC BANNERS</span></div>
  <div class="tile" style="left:746px;top:603px;height:252px;background:linear-gradient(160deg,#ededed,#b7aea4 70%,#8a3b20)" role="img" aria-label="Wall mural of a sculpted bonsai tree"><span class="tag">WALL MURALS</span></div>

  <div class="abs view-all">➕ View All Category</div>
</section>

<!-- About -->
<section class="section about">
  <div class="abs about-title">We're <span class="brand-name">TANDREL BANNERS</span> !</div>
  <div class="abs about-text">
    <p>Lorem Ipsum is simply dummy text of the printing and typesetting industry. Lorem Ipsum has been the industry's standard dummy text ever since the 1500s, when an unknown printer took a galley of type and scrambled it to make a type specimen book. It has survived not only five centuries, but also the leap into electronic typesetting, remaining essentially unchanged.</p>
    <p>It was popularised in the 1960s with the release of Typeset sheets containing Lorem Ipsum passages, and more recently with desktop layout software including versions of Lorem Ipsum.</p>
  </div>
  <span class="abs btn-solid">Read More</span>
  <div class="abs divider"></div>

  <div class="abs feature" style="top:72px">
    <div class="badge"><svg width="20" height="22" viewBox="0 0 20 22"><path d="M10 1l8 3v7c0 5-4 9-8 10-4-1-8-5-8-10V4z" fill="#333"/><text x="10" y="15" font-size="10" font-weight="700" text-anchor="middle" fill="#f6c500" font-family="Open Sans,sans-serif">$</text></svg></div>
    <h4>100% Quality and Price<br>Guarantee</h4>
    <p>Lorem Ipsum is simply dummy text of the printing and typesetting industry.</p>
  </div>
  <div class="abs feature-rule"></div>
  <div class="abs feature" style="top:205px">
    <div class="badge"><svg width="22" height="18" viewBox="0 0 22 18"><rect x="1" y="3" width="12" height="9" fill="#333"/><path d="M13 6h5l3 3v3h-8z" fill="#333"/><circle cx="5" cy="14" r="2.5" fill="#333"/><circle cx="17" cy="14" r="2.5" fill="#333"/></svg></div>
    <h4>Free Shipping<br>on all orders under $100</h4>
    <p>Lorem Ipsum is simply dummy text of the printing and typesetting industry.</p>
  </div>
</section>

<!-- Testimonials -->
<section class="section wow">
  <div class="head">
    <h2 class="section-title">CUSTOMER WOW</h2>
    <p class="section-sub">Lorem Ipsum is simply dummy text of the printing and typesetting</p>
    <div class="title-rule"></div>
  </div>

  <div class="quote" style="left:207px;top:131px;width:382px;height:176px;padding:26px 24px">Lorem Ipsum is simply dummy text of the printing and typesetting industry. Lorem Ipsum has been the industry's standard dummy text ever since the 1500s, when an unknown printer took a galley of type and scrambled it to make a type specimen book. It has survived not only five centuries, but also the leap into electronic typesetting.</div>
  <div class="avatar" role="img" aria-label="Customer portrait" style="left:252px;top:292px;width:90px;height:90px"></div>
  <div class="who" style="left:355px;top:318px">Oren Maddox<small>(General Manager)</small><span class="stars">★★★☆☆</span></div>

  <div class="quote" style="left:611px;top:135px;width:180px;height:136px">Lorem Ipsum is simply dummy text of the printing and typesetting industry. Lorem Ipsum has been the industry's standard dummy text ever since the.</div>
  <div class="avatar" role="img" aria-label="Customer portrait" style="left:630px;top:290px;width:47px;height:47px"></div>
  <div class="who" style="left:688px;top:298px;font-size:10px">Lyle Hartwin<small>(Quillon Inc.)</small><span class="stars">★★★☆☆</span></div>

  <div class="who" style="left:828px;top:128px;font-size:10px">Dana Crestley<small>(CFO, Brightmere Inc.)</small><span class="stars">★★★☆☆</span></div>
  <div class="avatar" role="img" aria-label="Customer portrait" style="left:923px;top:125px;width:47px;height:47px"></div>
  <div class="quote" style="left:811px;top:185px;width:180px;height:142px;padding-top:26px">Lorem Ipsum is simply dummy text of the printing and typesetting industry. Lorem Ipsum has been the industry's standard dummy text ever since the.</div>

  <div class="abs view-testi">➕ View All Testimonial</div>
</section>

<!-- Contact strip -->
<section class="section dedicated">
  <div class="head">
    <h2 class="section-title">WE'RE DEDICATED TO OUR CUSTOMERS</h2>
    <p class="section-sub">Lorem Ipsum is simply dummy text of the printing and typesetting</p>
    <div class="title-rule"></div>
  </div>
  <div class="contact-item" style="left:297px">
    <svg width="30" height="30" viewBox="0 0 30 30"><path d="M7 3l5 5-3 3c2 4 5 7 9 9l3-3 5 5-4 4C12 25 5 18 3 7z" fill="#222"/><path d="M17 5a8 8 0 0 1 8 8M17 1a12 12 0 0 1 12 12" fill="none" stroke="#222" stroke-width="2"/></svg>
    <h5>+61 255501482</h5><p>Available 24/7 - Call us any time.</p>
  </div>
  <div class="contact-item" style="left:499px">
    <svg width="30" height="30" viewBox="0 0 30 30"><rect x="2" y="7" width="26" height="17" fill="#222"/><path d="M2 7l13 10 13-10" fill="none" stroke="#fff" stroke-width="2"/></svg>
    <h5>Email</h5><p>Have a question? Let us help.</p>
  </div>
  <div class="contact-item" style="left:701px">
    <svg width="30" height="30" viewBox="0 0 30 30"><path d="M3 4h16v11H9l-4 4v-4H3z" fill="#222"/><path d="M21 9h6v11h-2v4l-4-4h-8v-3h8z" fill="#222"/></svg>
    <h5>Live Chat</h5><p>Online support to customers</p>
  </div>
  <div class="contact-item" style="left:903px">
    <svg width="30" height="30" viewBox="0 0 30 30"><path d="M15 2a12 12 0 0 1 0 24h-3l-5 4v-6A12 12 0 0 1 15 2z" fill="#222"/><text x="15" y="19" font-size="14" font-weight="700" text-anchor="middle" fill="#fff" font-family="Open Sans,sans-serif">?</text></svg>
    <h5>FAQ's</h5><p>Find your answers, if any problem.</p>
  </div>
</section>

<!-- Footer -->
<footer class="section footer">
  <svg class="abs rating" width="210" height="210" viewBox="0 0 210 210">
    <polygon fill="#f26522" points="105,0 115,22 133,4 137,28 159,15 156,39 181,33 172,56 196,56 182,76 205,82 186,97 206,109 185,121 202,137 180,143 192,163 168,164 175,187 152,183 153,207 132,196 127,219 111,204 105,226 95,204 78,219 73,196 52,207 53,183 30,187 37,164 13,163 25,143 3,137 20,121 -1,109 19,97 0,82 23,76 9,56 33,56 24,33 49,39 46,15 68,28 72,4 90,22" transform="scale(.93) translate(8,0)"/>
    <text x="105" y="70" text-anchor="middle" font-family="Montserrat,sans-serif" font-size="17" fill="#fff">Best Ratings</text>
    <text x="105" y="105" text-anchor="middle" font-size="28" fill="#f6c500">★★★★★</text>
    <text x="105" y="130" text-anchor="middle" font-family="Open Sans,sans-serif" font-size="13" fill="#fff">3.662 Reviews and</text>
    <text x="105" y="148" text-anchor="middle" font-family="Open Sans,sans-serif" font-size="13" fill="#fff">Counting!</text>
  </svg>

  <div class="foot-col" style="left:478px;width:110px">
    <h6>Quick Link</h6>
    <ul><li>About Us</li><li>Contact Us</li><li>Privacy Policy</li><li>Return Policy</li><li>Terms of Use</li><li>Sitemap</li><li>FAQ</li></ul>
  </div>
  <div class="foot-col" style="left:611px;width:110px">
    <h6>Service</h6>
    <ul><li>Design service</li><li class="current">About shipping</li><li>How to order</li><li>Refund and return</li></ul>
  </div>
  <div class="foot-col" style="left:744px;width:249px">
    <h6>Newsletter Signup</h6>
    <p style="font-size:9px;line-height:1.4">By subscribing to our mailing list you will be updated with the latest news from us.</p>
    <div class="field">Name</div>
    <div class="field">Email</div>
    <span class="send">SEND</span>
  </div>

  <div class="abs social">Get Social: <i></i><i></i><i></i><i></i></div>
</footer>

<div class="section bottombar">
  <span class="abs" style="left:207px;top:22px">© 2016 Tandrel Banners. All rights reserved.</span>
  <span class="abs" style="left:906px;top:22px;font-style:italic">Back to Top ⬆</span>
</div>

</body>
</html>
```